Quillfield Gallery Ridge Campus

Design cover and inside pages. - will fill in the rest later. I just have some ideas here. This is a marketing brochure for a new building - raising money. Should look professional - but this is an art gallery, so can have color. I wouldn't also mind seeing some chrome effects. I put some samples of fun ideas, but I am open. This is to get people exciting to give to the campaign to raise money for the new building
Target Market(s)
People who would like to donate to a new art gallery - the local community
Requirements
Must have
- The end product, after it is cut down from full bleed, should be 8.25 X 8.25.
Nice to have
- Should be modern and and exciting. The one thing is to show the problem and how we are going to solve it.. Something like "challenge" and resolution"..
- Would like it to go along with this idea of evolve - something new and improved and exciting.. with a very modern look. YOu will see that the logo is three different gradients of orange.. these can change to another color - it doesn't have to be orange.. I would like to see less orange used. The font on the old building is art deco.. so I see that the font for this should be non-serif
Should not have
- I have had designers use the logo as an overlay over pictures - I would like to get away from that.

```html
<!DOCTYPE html>
<html lang="en">
<head>
<meta charset="utf-8">
<title>Quillfield Gallery Guild – Brochure Cover and Spread</title>
<link rel="stylesheet" href="https://fonts.googleapis.com/css2?family=Open+Sans:wght@400;600;700;800&display=swap">
<style>
  :root {
    --backdrop: #ecebe8;
    --paper: #ffffff;
    --maroon: #4a1520;
    --maroon-deep: #35101a;
    --yellow: #f6e43a;
    --orange: #f2962a;
    --red: #e0453a;
    --text-light: #f3ebe6;
    --cover-ink: #3f3c3a;
    --brand-ink: #4a1520;
    --photo-warm: #b9ac96;
    --photo-cool: #7f8187;
    --plan-grey: #d9d9d9;
  }
  * { box-sizing: border-box; margin: 0; padding: 0; }
  html, body { width: 1200px; height: 808px; overflow: hidden; }
  body {
    background: var(--backdrop);
    position: relative;
    font-family: "Open Sans", Arial, sans-serif;
  }

  /* ---------- Cover ---------- */
  .cover {
    position: absolute; left: 24px; top: 239px;
    width: 330px; height: 330px;
    background: var(--paper);
    box-shadow: 0 6px 18px rgba(0,0,0,.18);
    overflow: hidden;
    display: flex; flex-direction: column;
  }
  .cover-image {
    position: relative; flex: 1;
    background: linear-gradient(135deg, #d9d1c2 0%, var(--photo-warm) 40%, var(--photo-cool) 75%, #a9abae 100%);
  }
  .cover-rule { position: absolute; background: rgba(255,255,255,.7); }
  .cover-rule.h { left: 0; right: 0; height: 1px; top: 58px; }
  .cover-rule.v { top: 0; bottom: 0; width: 1px; left: 198px; }
  .cover-title {
    position: absolute; left: 20px; top: 74px; width: 170px;
    color: var(--cover-ink);
    font-weight: 800; font-size: 22px; line-height: 1.1;
  }
  .cover-kicker {
    position: absolute; left: 210px; top: 16px; right: 14px;
    color: var(--cover-ink); font-size: 7.5px; font-weight: 600;
    line-height: 1.4; letter-spacing: .5px; text-transform: uppercase;
  }
  .cover-band {
    height: 58px; flex: none;
    background: var(--paper);
    border-top: 6px solid var(--orange);
    display: flex; align-items: center; gap: 10px; padding: 0 20px;
  }
  .cover-band .dot { width: 20px; height: 20px; border-radius: 50%; background: var(--orange); flex: none; }
  .cover-band .brand-name {
    font-weight: 600; color: var(--brand-ink);
    font-size: 12px; letter-spacing: 2px; line-height: 1.2;
  }

  /* ---------- Spread ---------- */
  .spread {
    position: absolute; left: 376px; top: 204px;
    width: 800px; height: 400px; display: flex;
    box-shadow: 0 6px 18px rgba(0,0,0,.2);
  }
  .page {
    position: relative; width: 400px; height: 400px; padding: 13px;
    background: linear-gradient(135deg, var(--yellow) 0%, var(--orange) 55%, var(--red) 100%);
  }
  .page-panel {
    position: relative; width: 100%; height: 100%;
    background: radial-gradient(circle at 30% 40%, var(--maroon) 0%, var(--maroon-deep) 100%);
    color: var(--text-light); padding: 16px 18px; overflow: hidden;
  }
  .page-heading { font-weight: 800; font-size: 20px; line-height: 1.05; color: #fff; }
  .body-copy { font-size: 7.4px; line-height: 1.45; margin-bottom: 7px; }
  .challenge { font-size: 7px; line-height: 1.45; }
  .challenge b, .body-copy b { font-weight: 700; color: #fff; }
  .photo { background: linear-gradient(160deg, #c9c3bb, #8c8178); border: 2px solid #fff; }

  .page-left .page-heading { margin-top: 6px; width: 150px; }
  .photo-strip { position: absolute; right: 8px; top: 16px; display: flex; gap: 3px; }
  .photo-strip .photo { width: 62px; height: 44px; }
  .page-left .intro { margin-top: 22px; }
  .challenge-cols { display: flex; gap: 12px; margin-top: 8px; }
  .challenge-cols .challenge { flex: 1; }

  .page-right .page-panel { padding-right: 118px; }
  .plan-column {
    position: absolute; right: 8px; top: 0; bottom: 0; width: 96px;
    display: flex; flex-direction: column; gap: 4px; padding: 22px 0 30px;
  }
  .plan-column .plan { flex: 1; background: linear-gradient(180deg, #f1f1f1, var(--plan-grey)); border: 2px solid #fff; }
  .page-right .page-heading { margin: 6px 0 18px; text-transform: uppercase; }
  .closing { font-size: 7.4px; font-weight: 700; color: #fff; margin-top: 4px; }
</style>
</head>
<body>

<section class="cover" aria-label="Brochure cover">
  <div class="cover-image" role="img" aria-label="Photograph of the gallery interior with display cases and framed artwork">
    <div class="cover-rule h"></div>
    <div class="cover-rule v"></div>
    <p class="cover-kicker">Campaign for a new gallery building</p>
    <h1 class="cover-title">Quillfield Gallery Ridge Campus</h1>
  </div>
  <div class="cover-band">
    <span class="dot"></span>
    <span class="brand-name">QUILLFIELD GALLERY GUILD</span>
  </div>
</section>

<section class="spread" aria-label="Inside spread">
  <article class="page page-left">
    <div class="page-panel">
      <div class="photo-strip">
        <div class="photo" role="img" aria-label="Photo of the current gallery building"></div>
        <div class="photo" role="img" aria-label="Photo of the gallery entrance"></div>
        <div class="photo" role="img" aria-label="Photo of an exhibition room"></div>
      </div>
      <h2 class="page-heading">a look to<br>the future...</h2>
      <p class="body-copy intro">The Quillfield Gallery has been operating since 1949 in the same building on the college campus. The space has served us well, but lighting, storage and climate control now limit the exhibits we can host and the artists we can invite.</p>
      <p class="body-copy">One of the long-term goals of the gallery is a new home at Quillfield Gallery Ridge Campus, built to museum standards for light and humidity, with room for an outdoor sculpture garden.</p>
      <div class="challenge-cols">
        <p class="challenge"><b>Challenge:</b> Many members and visitors have told us about the trouble of finding parking near the gallery. <b>Resolution:</b> The new site sits beside a large lot with easy access to the front doors.</p>
        <p class="challenge"><b>Challenge:</b> In past years, the college had to limit how long large works could stay on view. <b>Resolution:</b> Dedicated storage rooms will keep the collection safe between shows.</p>
        <p class="challenge"><b>Challenge:</b> Loading and unloading art is done through the main entrance. <b>Resolution:</b> A rear dock and wide service hall will move crates without closing the gallery.</p>
      </div>
    </div>
  </article>

  <article class="page page-right">
    <div class="page-panel">
      <div class="plan-column">
        <div class="plan" role="img" aria-label="Floor plan sketch of the new exhibition hall"></div>
        <div class="plan" role="img" aria-label="Floor plan sketch of the workshop wing"></div>
        <div class="plan" role="img" aria-label="Site plan of the new building"></div>
      </div>
      <h2 class="page-heading">bigger<br>exhibits...</h2>
      <p class="body-copy">The current moveable walls give about 180 linear feet of hanging space. The new exhibition hall will double that, with controlled lighting so delicate works can be shown safely. A new kitchen will be usable by staff and guests during receptions.</p>
      <p class="body-copy"><b>Challenge:</b> The front desk is shared by the receptionist, a work-study student and the gift shop. <b>Resolution:</b> A dedicated reception area and a separate shop will welcome visitors.</p>
      <p class="body-copy"><b>Challenge:</b> Framing and labels are prepared in a small back room. <b>Resolution:</b> A full workshop and art storage space will support every show.</p>
      <p class="closing">We hope you will join us in building a gallery for workshops and events!</p>
    </div>
  </article>
</section>

</body>
</html>
```